Resume for CEO

I need two formats of a resume created.

#1. It is 3 pages long and is the extended version.

#2. Is the 1 page resume.

Both should have the same styling. I am attaching the long and short version in word. I am also attaching a temporary picture for the resume. I will switch that out myself. Don't worry about keeping the sizing. It can be whatever you want.

There is a good website to use as a reference. http://brindlecvs.com/
The reason I am not using this site is because they don't give you the files for editing. They make you use them to edit.

Please feel free to ask questions. I"m excited to see the ideas that come up.

End format should be in AI with PDF's. I want 1 resume that is 3-4 pages and one that is 1 page. They should have the same style.

Dale

Reason: I have only received 2 designs. Hopefully I can get more submissions.

Reason: I need to get the design finalized and I will end the project.

```html
<!DOCTYPE html>
<html lang="en">
<head>
<meta charset="utf-8">
<title>Dale S. Holland — Resume</title>
<link rel="stylesheet" href="https://fonts.googleapis.com/css2?family=Arimo:wght@400;700&family=Libre+Baskerville:wght@700&display=swap">
<style>
  :root{
    --green:#1f4a2a;
    --green-text:#245232;
    --panel:#f0f0f1;
    --panel-edge:#d4d4d6;
    --bar-light:#f4f4f4;
    --bar-dark:#c9c9cb;
    --ink:#111;
    --white:#fff;
    --photo-a:#3a3026;
    --photo-b:#8a7a5e;
  }
  *{box-sizing:border-box;margin:0;padding:0}
  html,body{width:928px;height:1200px;overflow:hidden;background:var(--white)}
  body{position:relative;font-family:"Arimo",Arial,sans-serif;color:var(--ink)}

  .top-band{position:absolute;left:0;top:0;width:928px;height:24px;background:var(--green)}

  .name{position:absolute;left:0;top:36px;width:928px;text-align:center;
    font-family:"Libre Baskerville",Georgia,serif;font-weight:700;font-size:74px;letter-spacing:1px;
    color:var(--green-text);text-shadow:4px 4px 0 #b9b9b9;line-height:1}

  .title-line{position:absolute;left:0;top:128px;width:928px;display:flex;justify-content:center;align-items:center;gap:36px}
  .title-line .dots{letter-spacing:6px;font-weight:700;font-size:22px;color:var(--green-text);position:relative;top:-6px}
  .title-line .title{font-weight:700;font-size:24px;color:var(--ink)}

  .section-head{position:absolute;height:34px;display:flex;align-items:stretch;
    background:linear-gradient(to bottom,var(--bar-light),var(--bar-dark));
    border-bottom:3px solid var(--green)}
  .section-head .tab{background:var(--green);color:var(--white);
    font-family:"Libre Baskerville",Georgia,serif;font-weight:700;font-size:14px;
    display:flex;align-items:center;padding:0 34px 0 22px;
    clip-path:polygon(0 0,100% 0,calc(100% - 16px) 100%,0 100%)}
  .section-head .sub{color:var(--green-text);font-family:"Libre Baskerville",Georgia,serif;font-weight:700;
    font-size:14px;display:flex;align-items:center;padding-left:6px}

  .profile-head{left:50px;top:174px;width:826px}
  .profile-panel{position:absolute;left:50px;top:211px;width:826px;height:280px;background:var(--panel);
    border:3px solid var(--panel-edge);border-top:none}
  .profile-text{position:absolute;left:29px;top:32px;width:488px;font-size:16.6px;line-height:1.2}
  .photo{position:absolute;left:568px;top:21px;width:190px;height:246px;
    background:linear-gradient(160deg,var(--photo-b),var(--photo-a));
    box-shadow:6px 6px 0 #9c9c9c}

  .career-head{left:50px;top:510px;width:400px}
  .core-head{left:482px;top:510px;width:394px}
  .industry-head{left:482px;top:822px;width:394px}

  .lower-panel{position:absolute;left:50px;top:544px;width:826px;height:556px;background:var(--panel);
    border:3px solid var(--panel-edge);border-top:none}
  .divider{position:absolute;left:413px;top:30px;width:2px;height:454px;background:#cfcfd1}

  .achievements{position:absolute;left:24px;top:17px;width:350px;list-style:none}
  .achievements li{position:relative;padding-left:15px;font-size:15.6px;line-height:1.22;margin-bottom:14px}
  .achievements li::before{content:"•";position:absolute;left:0;top:0}

  .caps-list{position:absolute;list-style:none;left:447px;width:370px}
  .caps-list li{font-weight:700;font-size:14px;line-height:22.8px;padding-left:14px;position:relative}
  .caps-list li::before{content:"•";position:absolute;left:0}
  .competencies{top:10px}
  .specializations{top:328px}

  .footer{position:absolute;left:0;top:1122px;width:928px;height:78px;background:var(--green);color:var(--white);
    font-weight:700;font-size:17.5px;text-align:center;padding-top:14px;line-height:1.45}
</style>
</head>
<body>
  <div class="top-band"></div>

  <h1 class="name">DALE S. HOLLAND</h1>
  <div class="title-line">
    <span class="dots">•••••</span>
    <span class="title">CHIEF EXECUTIVE OFFICER&nbsp; / &nbsp;ENTREPRENEUR</span>
    <span class="dots">•••••</span>
  </div>

  <div class="section-head profile-head"><span class="tab">PROFILE</span></div>
  <section class="profile-panel">
    <p class="profile-text">Dynamic Chief Executive Officer with over 16 years of experience in providing strategic direction and leadership for organizations in multiple markets with unique situations. &nbsp; Extensive experience transforming companies into profitable and progressive organizations using proven systematic implementation. Offers comprehensive knowledge and operational experience with highly-engineered technical manufacturing companies, ecommerce and international brand building. Effectively identifies critical business drivers in multiple markets and industries, enabling growth opportunities within a variety of departments and ultimately complete business expansion.</p>
    <div class="photo" role="img" aria-label="Portrait photograph of the candidate in a dark suit"></div>
  </section>

  <div class="section-head career-head"><span class="tab">CAREER</span><span class="sub">ACHIEVEMENTS</span></div>
  <div class="section-head core-head"><span class="tab">CORE</span><span class="sub">COMPETENCIES</span></div>

  <section class="lower-panel">
    <ul class="achievements">
      <li>Constructed multiple start-up companies from ground-up utilizing organic growth strategies with little capital demonstrating consistent expansions and sales increase, accelerating into well-known international brands.</li>
      <li>Corporate restructuring and turnaround deployment, assisting several companies from decline and near insolvency into profitable states by streamlining the organization and renovating management, marketing, and sales strategies.</li>
      <li>Produced measurable year-after-year improvement under shifting conditions and economically depressed markets by adopting “lean mentality” and “just-in-time” strategies.</li>
      <li>Conceived and led revenue capture strategies, successfully achieving positive sales trajectories in addition to designing and sourcing innovative and industry-altering technologies.</li>
      <li>Rebuilt and rejuvenated leadership staff into unified, top-performing, and highly motivated teams. Utilizing these teams to secure strong international distribution by expanding businesses into international markets.</li>
    </ul>
    <div class="divider"></div>

    <ul class="caps-list competencies">
      <li>CHIEF EXECUTIVE OFFICER</li>
      <li>TURNAROUND</li>
      <li>ORGANIC BUSINESS GROWTH</li>
      <li>BRAND BUILDING</li>
      <li>BUSINESS DEVELOPMENT</li>
      <li>CONTRACT MANUFACTURING</li>
      <li>STRONG FINANCIAL ACCOUNTING</li>
      <li>CORPORATE RESTRUCTURING</li>
      <li>STRATEGIC SALES PLANNING</li>
      <li>KEY MANAGEMENT CONSTRUCTION</li>
      <li>MARKETING STRATEGIES</li>
    </ul>

    <ul class="caps-list specializations">
      <li>INTERNATIONAL BUSINESS</li>
      <li>OUTDOOR SPORTING GOODS &amp; ACTION SPORTS</li>
      <li>ECOMMERCE &amp; SPECIALTY RETAIL</li>
      <li>INT. DISTRIBUTION &amp; LOGISTICS</li>
      <li>SALES &amp; MARKETING STRATEGIES</li>
      <li>ACQUISITIONS &amp; INTEGRATIONS</li>
      <li>CORPORATE FUNDING</li>
      <li>CORPORATE RESTRUCTURING</li>
    </ul>
  </section>

  <div class="section-head industry-head"><span class="tab">INDUSTRY</span><span class="sub">SPECIALIZATIONS</span></div>

  <footer class="footer">
    4870 Willow Crest Ave. Ste. 210 - Carlsbad, CA 92008<br>
    (555) 014-2291 - daleholland22@mailbox.com
  </footer>
</body>
</html>
```